Powerpoint, Graphics for Sermon Series

I am starting a sermon series on the short letters if Scripture that are between Hebrews and Revelation. The sermon series will be called "Sifting Through Dusty Boxes: Lasting Lessons from Faded Pages."

Think about finding a packet of letters in an Attic. There is only the dialogue of the writer. We don't know exactly what the receivers were going through or even what their response to the letters were/are!

Target Market(s)

Local Church

Industry/Entity Type

Christian

Font styles to use
Serif
Sans Serif

Colors

Designer to choose colors to be used in the design.

Requirements
Must have
• Powerpoint Slide with Title -
• Background Slide -
• It would be great to have both JPG, PNG, and Photoshop/Indesign that can be used for powerpoint, both in 4x3 ration and wide... Need Title Slide with typography and background slide for text to go over the top of.
• Stick with the theme -- Sifting Through Dusty Boxes
• I am including our church logo, but don't feel like you need to use it in anyway.
Nice to have
• Social Media Slides - Square Slide, Facebook Header
• Greyscale Version?

```html
<!DOCTYPE html>
<html lang="en">
<head>
<meta charset="utf-8">
<title>Sifting Through Dusty Boxes – Sermon Series Title Slide</title>
<link href="https://fonts.googleapis.com/css2?family=Roboto+Slab:wght@500&family=Source+Sans+3:wght@600&display=swap" rel="stylesheet">
<style>
  :root {
    --paper-dark: #5b3a1f;
    --paper-mid: #9a6a3c;
    --paper-light: #c9a074;
    --accent-orange: #f29a0b;
    --slide-white: #ffffff;
    --haze-light: #f4f2ef;
    --haze-mid: #e3dfda;
    --title-ink: #5d4c40;
    --church-ink: #5a4433;
    --tagline-green: #5f8f2e;
  }
  html, body {
    margin: 0;
    padding: 0;
    width: 1200px;
    height: 900px;
    overflow: hidden;
    background: var(--slide-white);
  }
  .slide {
    position: relative;
    width: 1200px;
    height: 900px;
    overflow: hidden;
  }
  .slide-art {
    position: absolute;
    inset: 0;
    width: 1200px;
    height: 900px;
  }
  .series-title {
    position: absolute;
    right: 30px;
    top: 372px;
    margin: 0;
    text-align: right;
    font-family: "Roboto Slab", Georgia, serif;
    font-weight: 500;
    font-size: 38px;
    line-height: 58px;
    color: var(--title-ink);
  }
  .series-title span { display: block; }
  .church-mark {
    position: absolute;
    right: 36px;
    top: 700px;
    display: flex;
    align-items: center;
    gap: 16px;
  }
  .church-mark-square {
    width: 22px;
    height: 22px;
    background: var(--church-ink);
  }
  .church-name {
    margin: 0;
    font-family: "Roboto Slab", Georgia, serif;
    font-weight: 500;
    font-size: 34px;
    line-height: 1.1;
    color: var(--church-ink);
  }
  .church-tagline {
    position: absolute;
    right: 36px;
    top: 856px;
    margin: 0;
    font-family: "Source Sans 3", Arial, sans-serif;
    font-weight: 600;
    font-size: 20px;
    color: var(--tagline-green);
  }
</style>
</head>
<body>
  <main class="slide">
    <svg class="slide-art" viewBox="0 0 1200 900" xmlns="http://www.w3.org/2000/svg">
      <defs>
        <linearGradient id="letters-tone" x1="0" y1="0" x2="1" y2="1">
          <stop offset="0" stop-color="var(--paper-mid)"/>
          <stop offset="0.45" stop-color="var(--paper-light)"/>
          <stop offset="1" stop-color="var(--paper-dark)"/>
        </linearGradient>
        <linearGradient id="haze-tone" x1="0" y1="0" x2="1" y2="1">
          <stop offset="0" stop-color="var(--haze-light)"/>
          <stop offset="0.6" stop-color="var(--slide-white)"/>
          <stop offset="1" stop-color="var(--haze-mid)"/>
        </linearGradient>
      </defs>
      <rect class="letters-photo" x="0" y="0" width="1200" height="900" fill="url(#letters-tone)" role="img" aria-label="Close-up photograph of old handwritten letters on aged paper"/>
      <path class="divider-white" d="M572 0 Q420 430 668 900 L1200 900 L1200 0 Z" fill="var(--slide-white)"/>
      <path class="divider-orange" d="M584 0 Q432 430 680 900 L1200 900 L1200 0 Z" fill="var(--accent-orange)"/>
      <path class="sky-panel" d="M634 0 Q470 450 712 900 L1200 900 L1200 0 Z" fill="url(#haze-tone)" role="img" aria-label="Faint hazy photograph of three crosses on a hill against a pale sky"/>
    </svg>

    <h1 class="series-title">
      <span>Sifting Through Dusty Boxes</span>
      <span>Lasting Lessons from Faded Pages</span>
    </h1>

    <div class="church-mark">
      <div class="church-mark-square"></div>
      <p class="church-name">Cedar Hollow<br>Community Church</p>
    </div>
    <p class="church-tagline">Walking in Faith.</p>
  </main>
</body>
</html>
```